Infografiken für Rechtsfirma
Zielgruppe
Wir sind eine Rechtsfirma, welche sich mit dem europäischen Recht beschäftigt. Wir bieten Insolvenzen in unterschiedlichen Ländern an. Weiter beraten wir hinsichtlich des Vermögensschutzes. Wir helfen dabei, Vermögenswerte zu sichern. Für unseren Bereich Vermögensschutz benötigen wir eine Grafik, welche die Vorteile unseres Produkts direkt auf einen Blick erkennen lässt. Hierzu habe ich eine Grafik eines großen Mobilfunkherstellers beigefügt. Im gleichen Designe möchten wir diese Grafik haben.
Aufgabenstellung
Ich habe eine PDF-Datei (Vermögensschutz) beigefügt, aus welcher sich die Keyfacts ergeben. Diese müssen grafisch aufbereitet werden.

```html
<!DOCTYPE html>
<html lang="de">
<head>
<meta charset="utf-8">
<title>Vermögensschutz – Vorteile auf einen Blick</title>
<link rel="stylesheet" href="https://fonts.googleapis.com/css2?family=Arimo:wght@400;700&family=PT+Sans:wght@400&display=swap">
<style>
  :root {
    --bg: #ffffff;
    --ink: #1a1a1a;
    --muted: #7c7f87;
    --pink: #ec3f63;
    --crimson: #d21b4c;
    --orange: #fb9631;
    --coral: #ff6f55;
    --yellow: #f6bd16;
    --green: #8dbd55;
    --sea: #4fb38a;
    --teal: #1fb0bd;
    --purple: #7a0a6e;
    --magenta: #a8165c;
    --card: #ffffff;
  }
  html, body {
    margin: 0;
    padding: 0;
    width: 1200px;
    height: 800px;
    overflow: hidden;
    background: var(--bg);
  }
  .infosheet { display: block; width: 1200px; height: 800px; }
  .text-soft { font-family: "PT Sans", sans-serif; fill: var(--ink); }
  .text-strong { font-family: "Arimo", sans-serif; font-weight: 700; fill: var(--ink); }
  .text-plain { font-family: "Arimo", sans-serif; font-weight: 400; fill: var(--ink); }
  .segment-label { font-family: "Arimo", sans-serif; font-weight: 700; fill: #fff; font-size: 34px; }
  .asset-label { font-family: "PT Sans", sans-serif; font-size: 24px; fill: var(--ink); }
  .segment { stroke: #fff; stroke-width: 6; }
  .connector { fill: none; stroke-width: 8; stroke-linecap: round; stroke-linejoin: round; }
  .card { fill: var(--card); }
</style>
</head>
<body>
<svg class="infosheet" viewBox="0 0 2340 1560" xmlns="http://www.w3.org/2000/svg">
  <defs>
    <filter id="soft-shadow" x="-20%" y="-20%" width="140%" height="150%">
      <feDropShadow dx="3" dy="5" stdDeviation="7" flood-color="#000" flood-opacity=".14"/>
    </filter>
  </defs>

  <!-- Vorteile: Liste oben links -->
  <g class="benefit-list">
    <g class="benefit benefit--anonymity">
      <rect class="card" x="430" y="182" width="555" height="170" rx="85" filter="url(#soft-shadow)"/>
      <circle cx="437" cy="268" r="96" fill="var(--pink)"/>
      <circle cx="437" cy="268" r="64" fill="#fff"/>
      <text class="text-soft" x="437" y="279" font-size="30" text-anchor="middle">100%</text>
      <text class="text-soft" x="605" y="222" font-size="31">Anonymität</text>
      <text class="text-soft" x="585" y="273" font-size="31">Keine Rückschlüsse</text>
      <text class="text-soft" x="585" y="311" font-size="31">auf Sie möglich</text>
    </g>
    <g class="benefit benefit--transfer-tax">
      <rect class="card" x="430" y="375" width="555" height="170" rx="85" filter="url(#soft-shadow)"/>
      <circle cx="437" cy="460" r="96" fill="var(--orange)"/>
      <circle cx="437" cy="460" r="64" fill="#fff"/>
      <text class="text-soft" x="437" y="478" font-size="50" text-anchor="middle">0%</text>
      <text class="text-soft" x="580" y="443" font-size="31">Grunderwerbssteuer</text>
      <text class="text-soft" x="580" y="483" font-size="31">freie Einbringung</text>
    </g>
    <g class="benefit benefit--tax-optimisation">
      <rect class="card" x="430" y="567" width="555" height="170" rx="85" filter="url(#soft-shadow)"/>
      <circle cx="437" cy="652" r="96" fill="var(--green)"/>
      <circle cx="437" cy="652" r="64" fill="#fff"/>
      <path d="M412 654 l17 17 l33 -38" fill="none" stroke="var(--green)" stroke-width="10" stroke-linecap="round" stroke-linejoin="round"/>
      <text class="text-soft" x="580" y="622" font-size="31">Steueroptimierung</text>
      <text class="text-soft" x="580" y="660" font-size="31">für das laufende</text>
      <text class="text-soft" x="580" y="699" font-size="31">Einkommen</text>
    </g>
  </g>

  <!-- Sicherung von Vermögenswerten: Ringdiagramm oben rechts -->
  <g class="asset-ring">
    <g filter="url(#soft-shadow)">
      <path class="segment" d="M1617 151 A283 283 0 0 1 1817 234 L1746 305 A183 183 0 0 0 1617 251 Z" fill="var(--crimson)"/>
      <path class="segment" d="M1817 234 A283 283 0 0 1 1900 434 L1800 434 A183 183 0 0 0 1746 305 Z" fill="var(--orange)"/>
      <path class="segment" d="M1900 434 A283 283 0 0 1 1817 634 L1746 563 A183 183 0 0 0 1800 434 Z" fill="var(--coral)"/>
      <path class="segment" d="M1817 634 A283 283 0 0 1 1617 717 L1617 617 A183 183 0 0 0 1746 563 Z" fill="var(--teal)"/>
      <path class="segment" d="M1617 717 A283 283 0 0 1 1417 634 L1488 563 A183 183 0 0 0 1617 617 Z" fill="var(--green)"/>
      <path class="segment" d="M1417 634 A283 283 0 0 1 1334 434 L1434 434 A183 183 0 0 0 1488 563 Z" fill="var(--magenta)"/>
      <path class="segment" d="M1334 434 A283 283 0 0 1 1417 234 L1488 305 A183 183 0 0 0 1434 434 Z" fill="var(--purple)"/>
      <path class="segment" d="M1417 234 A283 283 0 0 1 1617 151 L1617 251 A183 183 0 0 0 1488 305 Z" fill="var(--pink)"/>
    </g>
    <circle cx="1617" cy="434" r="160" fill="#fff"/>
    <g class="trend-icon" fill="var(--muted)">
      <rect x="1592" y="362" width="11" height="19"/>
      <rect x="1608" y="354" width="11" height="27"/>
      <rect x="1624" y="348" width="11" height="33"/>
      <path d="M1590 352 L1606 340 L1620 350 L1644 334" fill="none" stroke="var(--muted)" stroke-width="5"/>
      <path d="M1638 330 L1652 330 L1650 343 Z"/>
    </g>
    <text class="text-soft" x="1617" y="428" font-size="36" text-anchor="middle">Sicherung von</text>
    <text class="text-soft" x="1607" y="472" font-size="36" text-anchor="middle">Vermögenswerten</text>

    <text class="segment-label" transform="translate(1530 230) rotate(-22)" text-anchor="middle">Auto</text>
    <text class="segment-label" transform="translate(1820 337) rotate(68)" text-anchor="middle">Flugz</text>
    <text class="segment-label" transform="translate(1703 666) rotate(-22)" text-anchor="middle">Uhren</text>
    <text class="segment-label" transform="translate(1390 492) rotate(68)" text-anchor="middle">Boot</text>

    <text class="asset-label" x="1357" y="214" text-anchor="middle">Immobilien</text>
    <text class="asset-label" x="1885" y="214" text-anchor="middle">Barvermögen</text>
    <text class="asset-label" x="1307" y="634" text-anchor="middle">Kryptowährung</text>
    <text class="asset-label" x="1916" y="634" text-anchor="middle">Firmenanteile</text>
  </g>

  <!-- Schutz vor Ansprüchen Dritter: unten links -->
  <g class="claims-shield">
    <g class="connectors">
      <path class="connector" stroke="var(--pink)" d="M560 960 L600 910 L830 910"/>
      <path class="connector" stroke="var(--crimson)" d="M625 1043 L895 1043"/>
      <path class="connector" stroke="var(--yellow)" d="M655 1162 L945 1162"/>
      <path class="connector" stroke="var(--yellow)" d="M600 1292 L910 1292"/>
      <path class="connector" stroke="var(--coral)" d="M525 1350 L570 1420 L920 1420"/>
      <path d="M830 898 L852 910 L830 922 Z" fill="var(--pink)"/>
      <path d="M895 1031 L917 1043 L895 1055 Z" fill="var(--crimson)"/>
      <path d="M945 1150 L967 1162 L945 1174 Z" fill="var(--yellow)"/>
      <path d="M910 1280 L932 1292 L910 1304 Z" fill="var(--yellow)"/>
      <path d="M920 1408 L942 1420 L920 1432 Z" fill="var(--coral)"/>
    </g>

    <g filter="url(#soft-shadow)">
      <path class="segment" d="M302 1003 A205 205 0 0 1 592 1003 L547 1048 A142 142 0 0 0 347 1048 Z" fill="var(--pink)"/>
      <path class="segment" d="M592 1003 A205 205 0 0 1 652 1148 L589 1148 A142 142 0 0 0 547 1048 Z" fill="var(--purple)"/>
      <path class="segment" d="M652 1148 A205 205 0 0 1 592 1293 L547 1248 A142 142 0 0 0 589 1148 Z" fill="var(--teal)"/>
      <path class="segment" d="M592 1293 A205 205 0 0 1 302 1293 L347 1248 A142 142 0 0 0 547 1248 Z" fill="var(--orange)"/>
      <path class="segment" d="M302 1293 A205 205 0 0 1 242 1148 L305 1148 A142 142 0 0 0 347 1248 Z" fill="var(--sea)"/>
      <path class="segment" d="M242 1148 A205 205 0 0 1 302 1003 L347 1048 A142 142 0 0 0 305 1148 Z" fill="var(--purple)"/>
    </g>
    <circle cx="447" cy="1148" r="142" fill="#fff"/>
    <g class="tick-icon">
      <circle cx="440" cy="1070" r="19" fill="var(--muted)"/>
      <path d="M432 1070 l6 6 l10 -11" fill="none" stroke="#fff" stroke-width="4"/>
    </g>
    <text class="text-strong" x="455" y="1128" font-size="35" text-anchor="middle">Schutz vor</text>
    <text class="text-strong" x="449" y="1168" font-size="35" text-anchor="middle">Ansprüchen</text>
    <text class="text-strong" x="449" y="1208" font-size="35" text-anchor="middle">Dritter</text>

    <text class="text-strong" x="660" y="873" font-size="35" text-anchor="middle">Bank</text>
    <text class="text-strong" x="738" y="1000" font-size="35" text-anchor="middle">Finanzamt</text>
    <text class="text-strong" x="798" y="1125" font-size="35" text-anchor="middle">Bürgschaften</text>
    <text class="text-strong" x="734" y="1252" font-size="35" text-anchor="middle">Klage</text>
    <text class="text-strong" x="722" y="1380" font-size="35" text-anchor="middle">Sozialversicherung</text>
  </g>

  <!-- Steuerliche Vorteile: Bänder unten rechts -->
  <g class="tax-bands">
    <g class="band band--exit-tax">
      <rect x="1290" y="810" width="682" height="180" rx="90" fill="var(--orange)"/>
      <circle cx="1388" cy="900" r="70" fill="#fff" filter="url(#soft-shadow)"/>
      <text class="text-strong" x="1388" y="920" font-size="60" text-anchor="middle">0%</text>
      <text class="text-plain" x="1713" y="867" font-size="35" text-anchor="middle">Wegzugsbesteuerung</text>
      <text class="text-plain" x="1732" y="912" font-size="35" text-anchor="middle">Freiheit</text>
    </g>
    <g class="band band--inheritance-tax">
      <rect x="1290" y="1027" width="682" height="180" rx="90" fill="var(--sea)"/>
      <circle cx="1877" cy="1117" r="70" fill="#fff" filter="url(#soft-shadow)"/>
      <text class="text-strong" x="1877" y="1137" font-size="60" text-anchor="middle">0%</text>
      <text class="text-plain" x="1513" y="1104" font-size="35" text-anchor="middle">Erbschaftssteuer</text>
    </g>
    <g class="band band--insolvency">
      <rect x="1290" y="1240" width="682" height="180" rx="90" fill="var(--crimson)"/>
      <circle cx="1388" cy="1330" r="70" fill="#fff" filter="url(#soft-shadow)"/>
      <text class="text-strong" x="1388" y="1347" font-size="48" text-anchor="middle">100%</text>
      <text class="text-plain" x="1595" y="1278" font-size="34">Insolvenz sicher</text>
      <text class="text-plain" x="1595" y="1318" font-size="34">Kein Zugriff vom</text>
      <text class="text-plain" x="1595" y="1358" font-size="34">Insolvenzverwalter</text>
    </g>
  </g>
</svg>
</body>
</html>
```